2023 TRW Festival Form

• We are looking for a one-page form front and back. Something that comes that way, and we don’t have to merge it.
• Must be a fillable form, PDF version.
• The form will need to be editable; we will make minor changes as needed to the form, mainly contact information.
• Please add pictures, descriptions, and a registration area that includes a grand total donated.
• Attached are descriptions, links, and additional information that may help you develop a fluid registration form for us.

```html
<!DOCTYPE html>
<html lang="en">
<head>
<meta charset="utf-8">
<title>2023 TRW Festival Form</title>
<link href="https://fonts.googleapis.com/css2?family=Lilita+One&family=Montserrat:ital,wght@0,400;0,500;0,600;0,700;0,800;1,600;1,700;1,800&display=swap" rel="stylesheet">
<style>
:root{
  --blue:#1b4fb0;
  --blue-dark:#123e91;
  --gold:#e2b677;
  --gold-deep:#c8924a;
  --brown:#4a3116;
  --ink:#1e1e22;
  --footer:#1e2026;
  --red:#e0302a;
  --lavender:#c9cde8;
  --rule:#2a5cc0;
  --bg:#e6e8ec;
  --white:#ffffff;
}
*{box-sizing:border-box;margin:0;padding:0}
html,body{width:1200px;height:3153px;overflow:hidden}
body{background:var(--bg);font-family:"Montserrat",sans-serif;color:var(--ink);position:relative}
.page{position:absolute;left:60px;width:1080px;height:1530px;background:var(--white);overflow:hidden;box-shadow:0 6px 24px rgba(0,0,0,.12)}
.page-front{top:30px}
.page-back{top:1593px}
.t{position:absolute;white-space:nowrap}
.header{position:absolute;left:0;top:0;width:1080px;background:linear-gradient(180deg,var(--blue) 0%,var(--blue-dark) 100%)}
.torn{position:absolute;left:0;width:1080px;height:24px}
.brand{position:absolute;color:var(--white);font-family:"Montserrat",sans-serif;font-weight:700;line-height:1.1;display:flex;align-items:center;gap:10px}
.brand-dot{width:14px;height:14px;border-radius:50%;background:var(--gold);flex:none}
.title{font-family:"Lilita One",sans-serif;color:var(--white);letter-spacing:1px}
.title sup{font-size:.55em;vertical-align:.7em}
.title-frame{position:absolute;left:284px;top:58px;width:756px;height:146px;border:2px solid var(--gold);border-radius:14px}
.date-pill{position:absolute;background:linear-gradient(180deg,#f3d4a2,var(--gold-deep));color:var(--brown);font-family:"Lilita One",sans-serif;display:flex;align-items:center;justify-content:center;border-radius:4px;white-space:nowrap}
.photo{position:absolute;border-radius:8px}
.ribbon{position:absolute;background:var(--gold);color:var(--blue-dark);font-weight:800;font-size:17px;display:flex;align-items:center;justify-content:center}
.intro{position:absolute;left:508px;top:294px;width:540px;font-size:18px;line-height:22px;font-weight:500}
.intro b{color:var(--blue);font-weight:700}
.banner{position:absolute;background:var(--blue);color:var(--white);font-weight:800;display:flex;align-items:center;justify-content:center;clip-path:polygon(3% 0,100% 0,97% 100%,0 100%)}
.agenda-row{position:absolute;left:508px;width:492px;height:34px;border-bottom:2px solid var(--rule);display:flex;align-items:center}
.agenda-time{background:#111;color:var(--white);font-weight:600;font-size:18px;height:32px;display:flex;align-items:center;padding-left:16px;flex:none;white-space:nowrap}
.agenda-what{font-size:16px;font-weight:500;padding-left:26px;white-space:nowrap}
.field{position:absolute;left:66px;width:418px;height:38px;border:2px solid #222;border-radius:7px;font-size:19px;font-weight:600;padding-left:14px;display:flex;align-items:center}
.note{position:absolute;font-size:11px;color:#333;line-height:14px;white-space:nowrap}
.q{position:absolute;font-weight:600;font-size:18px;white-space:nowrap}
.box{display:inline-block;width:24px;height:24px;background:var(--lavender);vertical-align:middle;margin:0 24px 0 12px}
.attend{position:absolute;left:66px;top:1082px;width:424px;height:62px;background:var(--blue);border-radius:6px;color:#fff;font-weight:600;font-size:16px;line-height:21px;padding:10px 20px;white-space:nowrap}
.guest-line{position:absolute;left:66px;width:424px;height:32px;border-bottom:2px solid var(--rule)}
.num{position:absolute;left:0;bottom:2px;width:26px;height:22px;background:var(--blue);color:#fff;font-size:14px;font-weight:700;display:flex;align-items:center;justify-content:center}
.pill{position:absolute;background:var(--blue);color:#fff;font-weight:600;border-radius:4px;display:flex;align-items:center;padding-left:14px;white-space:nowrap}
.level{position:absolute;left:586px;width:410px;display:flex;justify-content:space-between;font-size:14px;font-weight:600}
.level span:last-child{color:var(--blue);font-weight:700;font-size:16px;width:80px}
.card{position:absolute;left:582px;top:1080px;width:412px;height:204px;border:2px solid #333;border-radius:14px}
.mini{position:absolute;width:64px;height:32px;border:2px solid #444}
.lbl{position:absolute;font-size:15px;font-weight:700;white-space:nowrap}
.uline{position:absolute;height:1.5px;background:#888}
.total{position:absolute;left:540px;top:1310px;width:452px;height:44px;display:flex;border:1.5px solid #888}
.total-label{width:260px;background:var(--gold);color:var(--brown);font-weight:700;font-size:20px;display:flex;align-items:center;padding-left:14px;white-space:nowrap}
.total-value{flex:1;font-weight:700;font-size:20px;display:flex;align-items:center;padding-left:10px}
.footer{position:absolute;left:0;top:1424px;width:1080px;height:106px;background:var(--footer)}
.footer-left{position:absolute;left:0;top:0;width:360px;height:106px;background:var(--blue);clip-path:polygon(0 0,100% 0,88% 100%,0 100%)}
.q-tab{position:absolute;left:40px;top:1398px;width:130px;height:26px;background:var(--gold);color:var(--brown);font-weight:800;font-style:italic;font-size:14px;display:flex;align-items:center;justify-content:center;clip-path:polygon(8% 0,92% 0,100% 100%,0 100%)}
.contact{position:absolute;left:40px;top:16px;color:#fff;font-size:19px;font-weight:600;line-height:26px;white-space:nowrap}
.deadline{position:absolute;left:378px;top:12px;color:#fff;font-size:12.5px;line-height:17px;width:470px;white-space:nowrap}
.deadline .gold{color:var(--gold);font-weight:600;font-size:14px}
.deadline i{font-weight:700;font-size:15px}
.deadline i b{color:var(--gold)}
.mail{position:absolute;left:866px;top:22px;color:#fff;font-size:12.5px;line-height:16px;padding-left:14px;border-left:1px solid #666;white-space:nowrap}
.mail b{color:var(--gold);font-weight:700;font-size:13px}
.events-echo{position:absolute;left:0;width:1080px;top:172px;text-align:center;font-family:"Lilita One",sans-serif;font-size:80px;color:#eef1f8;letter-spacing:6px}
.events-title{position:absolute;left:0;width:1080px;top:176px;text-align:center;font-family:"Lilita One",sans-serif;font-size:52px;color:var(--blue-dark);letter-spacing:2px}
.day-tag{position:absolute;background:var(--gold-deep);color:#fff;font-weight:800;font-size:19px;padding-left:16px;display:flex;align-items:center;height:32px;clip-path:polygon(0 0,88% 0,100% 100%,0 100%)}
.ev-head{position:absolute;color:var(--blue);font-weight:800;font-style:italic;font-size:22px;white-space:nowrap}
.ev-head small{font-size:14px;font-weight:600;letter-spacing:.5px}
.ev-text{position:absolute;font-size:14px;line-height:18px;font-weight:500}
.tk{position:absolute;font-size:14px;line-height:18px;font-weight:500;padding-left:22px;white-space:nowrap}
.tk svg{position:absolute;left:0;top:2px;width:14px;height:14px}
.bul{position:absolute;font-size:14px;line-height:18px;padding-left:16px;font-weight:500;white-space:nowrap}
.bul::before{content:"";position:absolute;left:2px;top:5px;border-left:7px solid var(--blue);border-top:4px solid transparent;border-bottom:4px solid transparent}
.red{position:absolute;color:var(--red);font-size:11.5px;line-height:14px;white-space:nowrap}
.blank{position:absolute;font-size:15px;color:var(--blue);font-weight:600;white-space:nowrap}
.blank i{display:inline-block;border-bottom:1.5px solid var(--blue);vertical-align:bottom}
.vrule{position:absolute;width:1px;background:#cfd4de}
.hrule{position:absolute;height:1px;background:#cfd4de}
</style>
</head>
<body>
<svg width="0" height="0" style="position:absolute">
  <symbol id="tick" viewBox="0 0 16 16"><circle cx="8" cy="8" r="6.5" fill="none" stroke="#1b4fb0" stroke-width="1.6"/><path d="M4.8 8.2l2.2 2.2 4.8-5" fill="none" stroke="#1b4fb0" stroke-width="1.8" stroke-linecap="round"/></symbol>
</svg>

<!-- FRONT -->
<section class="page page-front">
  <header class="header" style="height:254px">
    <div class="brand" style="left:40px;top:104px;font-size:22px"><span class="brand-dot"></span><span>Tri-River Wing<br>Federation</span></div>
    <div class="title-frame"></div>
    <div class="t title" style="left:330px;top:98px;font-size:56px">25<sup>th</sup> Annual TRW Festival</div>
    <div class="date-pill" style="left:390px;top:170px;width:560px;height:58px;font-size:38px">October 6th &amp; 7th, 2023</div>
    <svg class="torn" style="bottom:-1px" viewBox="0 0 1080 24" preserveAspectRatio="none"><path fill="#fff" d="M0 14 L40 8 L80 16 L130 6 L170 14 L230 9 L280 17 L340 7 L390 15 L450 8 L510 16 L560 7 L620 14 L680 9 L730 17 L790 6 L850 15 L900 8 L960 16 L1020 7 L1080 13 L1080 24 L0 24Z"/></svg>
  </header>

  <div class="photo" role="img" aria-label="Photo of the hotel tower with autumn trees" style="left:60px;top:294px;width:394px;height:394px;background:linear-gradient(180deg,#8fb4de 0%,#c9b79a 45%,#9b7d5a 70%,#b5482c 100%)"></div>
  <div class="ribbon" style="left:44px;top:314px;width:410px;height:40px">RESERVE YOUR HOTEL ROOM EARLY!</div>

  <p class="intro">Call Harbor Gate at <b>1 (800) 555-0142 or (859) 555-0188</b> Book by September 15th to make your room reservations. Mention the Tri-River Wing Federation or TRW for your room block.</p>

  <div class="banner" style="left:508px;top:388px;width:508px;height:38px;font-size:22px;justify-content:flex-start;padding-left:50px">AGENDA</div>
  <div class="agenda-row" style="top:446px"><span class="agenda-time" style="width:142px">1:30 PM</span><span class="agenda-what">Set up Silent Auction</span></div>
  <div class="agenda-row" style="top:496px"><span class="agenda-time" style="width:142px">4:30 PM</span><span class="agenda-what">Registration opens</span></div>
  <div class="agenda-row" style="top:546px"><span class="agenda-time" style="width:142px">5:00 PM</span><span class="agenda-what">ilent auction/music/cash bar opens</span></div>
  <div class="agenda-row" style="top:598px"><span class="agenda-time" style="width:142px">6:00 PM</span><span class="agenda-what">Annual Meeting and Awards Banquet</span></div>
  <div class="agenda-row" style="top:648px"><span class="agenda-time" style="width:208px">8:45 PM - 11:00 PM</span><span class="agenda-what">Moonlight Howl event</span></div>

  <div class="banner" style="left:70px;top:726px;width:940px;height:44px;font-size:32px">REGISTRATION PORTION OF THE FORM</div>

  <div class="note" style="left:200px;top:804px;width:284px;text-align:right">As it should appear on sponsorship information</div>
  <div class="field" style="top:820px">Company/ Contact</div>
  <div class="field" style="top:874px">Email</div>
  <div class="field" style="top:922px">Best Phone</div>
  <div class="q" style="left:72px;top:992px">ARE YOU ATTENDING? <span style="margin-left:24px">YES</span><span class="box"></span>NO<span class="box"></span></div>
  <div class="note" style="left:72px;top:1032px">*Most people will donate but will not attend<br>So I really need to know who's coming.</div>
  <div class="attend">ATTENDANCE WILL NOT BE GIVEN,<br>ONLY DONATIONS, OR DONATIONS FOR.</div>
  <div class="field" style="top:1158px">Guest Names</div>
  <div class="note" style="left:66px;top:1214px">As they should appear on name badges. Fill out only for those planning to attend</div>
  <div class="guest-line" style="top:1232px"><span class="num">1</span></div>
  <div class="guest-line" style="top:1266px"><span class="num">2</span></div>
  <div class="guest-line" style="top:1300px"><span class="num">3</span></div>
  <div class="guest-line" style="top:1334px"><span class="num">4</span></div>

  <div class="pill" style="left:586px;top:804px;width:418px;height:34px;font-size:19px;padding-left:34px">SPONSORSHIPS LEVELS</div>
  <div class="level" style="top:856px"><span>DIAMOND &nbsp;SPONSOR</span><span>$ 5,000</span></div>
  <div class="level" style="top:888px"><span>GOLDEN EGG SPONSOR</span><span>$ 3,000</span></div>
  <div class="level" style="top:918px"><span>SILVER CHICKEN SPONSOR</span><span>$ 2,000</span></div>
  <div class="level" style="top:950px"><span>BRONZE TURKEY SPONSOR</span><span>$ 1,000</span></div>
  <div class="level" style="top:980px"><span>FRIEND OF TRW</span><span>$ 500</span></div>
  <div class="t" style="left:586px;top:1022px;font-size:15px;line-height:18px;color:#333">The TRW Is a nonprofit organization, and your<br>donations are tax-deductible</div>

  <div class="card"></div>
  <div class="lbl" style="left:606px;top:1096px">Credit Card</div>
  <div class="mini" style="left:606px;top:1124px"></div>
  <div class="mini" style="left:702px;top:1124px"></div>
  <div class="mini" style="left:802px;top:1124px"></div>
  <div class="mini" style="left:902px;top:1124px"></div>
  <div class="lbl" style="left:606px;top:1170px">Exp. Date</div>
  <div class="lbl" style="left:728px;top:1170px">CVC</div>
  <div class="lbl" style="left:852px;top:1170px">Billing Zip Code</div>
  <div class="uline" style="left:606px;top:1204px;width:100px"></div>
  <div class="uline" style="left:728px;top:1204px;width:86px"></div>
  <div class="uline" style="left:852px;top:1204px;width:92px"></div>
  <div class="lbl" style="left:606px;top:1228px">Name on Card</div>
  <div class="uline" style="left:606px;top:1264px;width:364px"></div>

  <div class="total"><span class="total-label">Total Donated to TRW</span><span class="total-value">$</span></div>
  <div class="t" style="left:540px;top:1366px;font-size:14px;font-weight:700;line-height:18px">Sponsorship, Banquet Entertainment, Trade Show, Sporting<br>Clay, Golf Scramble, Farm and Distillery Tour &amp; Spa Day</div>

  <div class="q-tab">QUESTIONS</div>
  <footer class="footer">
    <div class="footer-left"></div>
    <div class="contact">CONTACT DANA WHITLOCK<br>270-555-0163<br>dwhitlock@triverwing.org</div>
    <div class="deadline"><span class="gold">DEADLINE FOR REGISTRATION: September 15, 2022</span><br>Make checks payable to the Tri-River Wing Federation or pay via<br>credit card using the Registration form.EmailRegistration Forms to<br><i>Email Registration Forms to: <b>dwhitlock@triverwing.org</b></i></div>
    <div class="mail">Mail payment and<br>this registration form to<br><b>410 Maple Station,<br>Bardwell, KY 42023</b></div>
  </footer>
</section>

<!-- BACK -->
<section class="page page-back">
  <header class="header" style="height:160px">
    <div class="brand" style="left:50px;top:52px;font-size:18px"><span class="brand-dot"></span><span>Tri-River Wing<br>Federation</span></div>
    <div class="t title" style="left:284px;top:26px;font-size:56px">25<sup>th</sup> Annual TRW Festival</div>
    <div class="date-pill" style="left:284px;top:100px;width:676px;height:32px;font-size:18px;letter-spacing:.5px">October 6th &amp; 7th, 2023 &nbsp;|&nbsp; Lexington, KY at the Harbor Gate Lodge</div>
    <svg class="torn" style="bottom:-1px" viewBox="0 0 1080 24" preserveAspectRatio="none"><path fill="#fff" d="M0 12 L50 7 L100 15 L150 6 L210 14 L260 8 L320 16 L370 7 L430 14 L490 8 L540 16 L600 7 L650 14 L710 9 L770 16 L820 6 L880 15 L940 8 L1000 16 L1080 10 L1080 24 L0 24Z"/></svg>
  </header>

  <div class="events-echo">EVENTS</div>
  <div class="events-title">EVENTS</div>

  <div class="vrule" style="left:360px;top:250px;height:1100px"></div>
  <div class="vrule" style="left:726px;top:250px;height:1100px"></div>
  <div class="hrule" style="left:20px;top:904px;width:324px"></div>
  <div class="hrule" style="left:740px;top:772px;width:330px"></div>

  <!-- Friday -->
  <div class="day-tag" style="left:36px;top:250px;width:176px">FRIDAY</div>
  <div class="photo" role="img" aria-label="Photo of racehorses and jockeys on the turf" style="left:36px;top:282px;width:288px;height:224px;border-radius:0;background:linear-gradient(180deg,#4f6f3c 0%,#6f5a3e 55%,#3f6a2c 100%)"></div>
  <div class="ev-head" style="left:36px;top:520px">RIDGELAND TAILGATING</div>
  <div class="ev-text" style="left:36px;top:550px;width:300px">Complimentary Meal &amp; Ridgeland Grandstand Reserved Seating included.</div>
  <div class="tk" style="left:36px;top:620px"><svg><use href="#tick"/></svg>Food and fun 11:00 a.m.-1:00 p.m. EST</div>
  <div class="tk" style="left:36px;top:648px"><svg><use href="#tick"/></svg>Races start at 1:05 p.m.</div>
  <div class="pill" style="left:36px;top:680px;width:194px;height:26px;font-size:14px">Cost per person $50</div>
  <div class="red" style="left:36px;top:720px">Must have the email address of<br>the person attending.</div>
  <div class="blank" style="left:36px;top:756px">Name <i style="width:150px;margin-left:16px"></i></div>
  <div class="blank" style="left:36px;top:784px">Email <i style="width:150px;margin-left:16px"></i></div>
  <div class="t" style="left:36px;top:814px;font-size:15px;font-weight:700">Sponsors</div>
  <div class="tk" style="left:36px;top:842px"><svg><use href="#tick"/></svg>Northvale Animal Health Event sponsor</div>
  <div class="tk" style="left:36px;top:870px"><svg><use href="#tick"/></svg>Local Beverages donated by Brightgrain</div>

  <div class="photo" role="img" aria-label="Photo of a singer and pianist performing on a lit stage" style="left:36px;top:930px;width:288px;height:224px;border-radius:0;background:linear-gradient(160deg,#0b1f4a 0%,#1f4fa0 50%,#0a1636 100%)"></div>
  <div class="ev-head" style="left:36px;top:1172px">BANQUET <small>(SATURDAY)</small></div>
  <div class="ev-text" style="left:36px;top:1204px;white-space:nowrap">Awards Banquet and Entertainment ticket</div>
  <div class="pill" style="left:36px;top:1236px;width:170px;height:26px;font-size:14px">$150 per person</div>
  <div class="tk" style="left:36px;top:1276px;font-weight:700"><svg><use href="#tick"/></svg>Entertainment</div>
  <div class="bul" style="left:58px;top:1302px">Moonlight Howl</div>
  <div class="bul" style="left:58px;top:1326px">Join us for fun, games, music, and<br>around $3,000 in prizes!</div>

  <!-- Saturday -->
  <div class="day-tag" style="left:394px;top:250px;width:176px">SATURDAY</div>
  <div class="photo" role="img" aria-label="Photo of a gloved hand placing a golf ball on a tee" style="left:394px;top:282px;width:290px;height:224px;border-radius:0;background:linear-gradient(180deg,#d9e6c6 0%,#8fb25a 50%,#3f7a28 100%)"></div>
  <div class="ev-head" style="left:394px;top:522px">GOLF</div>
  <div class="ev-text" style="left:394px;top:554px;width:310px">The scramble will be held at Harbor Gate Lodge Golf Club, located at 900 Meadow Pike, Lexington, KY, 40511, (859) 555-0188.</div>
  <div class="pill" style="left:394px;top:648px;width:236px;height:26px;font-size:14px">Fees for scramble are $125.</div>
  <div class="t" style="left:394px;top:700px;font-size:16px;font-weight:600">Names of Golfers</div>
  <div class="guest-line" style="left:394px;top:712px;width:290px"><span class="num" style="width:18px;height:18px;font-size:12px">1</span></div>
  <div class="guest-line" style="left:394px;top:746px;width:290px"><span class="num" style="width:18px;height:18px;font-size:12px">2</span></div>
  <div class="guest-line" style="left:394px;top:780px;width:290px"><span class="num" style="width:18px;height:18px;font-size:12px">3</span></div>
  <div class="guest-line" style="left:394px;top:814px;width:290px"><span class="num" style="width:18px;height:18px;font-size:12px">4</span></div>
  <div class="red" style="left:394px;top:862px">Must have the email address of<br>the person playing.</div>
  <div class="blank" style="left:394px;top:906px"><span class="bul" style="position:relative;padding-left:16px">Email</span><i style="width:214px;margin-left:10px"></i></div>
  <div class="blank" style="left:394px;top:940px"><span class="bul" style="position:relative;padding-left:16px">Average Score</span><i style="width:138px;margin-left:10px"></i></div>
  <div class="tk" style="left:394px;top:984px"><svg><use href="#tick"/></svg>Registration will begin Saturday,<br>October 7th, at 7:45 AM ET, and<br>we will tee off at 8:30 AM. ET</div>
  <div class="tk" style="left:394px;top:1060px"><svg><use href="#tick"/></svg>Lunch, Beverage cart drinks, and<br>snacks are included.</div>
  <div class="t" style="left:394px;top:1112px;font-size:15px;font-weight:700">Sponsors</div>
  <div class="tk" style="left:394px;top:1142px"><svg><use href="#tick"/></svg>Renway - Golf Towel</div>
  <div class="tk" style="left:394px;top:1170px"><svg><use href="#tick"/></svg>Fieldmark Labs – lunch</div>
  <div class="tk" style="left:394px;top:1198px"><svg><use href="#tick"/></svg>Ridgecrest Design- drink cart</div>
  <div class="ev-head" style="left:394px;top:1252px;line-height:28px">STATIC TRADE SHOW<br>BOOTH REQUESTS <small>(SATURDAY)</small></div>
  <div class="pill" style="left:394px;top:1314px;width:276px;height:26px;font-size:14px">Trade Show Booth (6 ft table) $100</div>

  <!-- Spa & Sporting Clay -->
  <div class="photo" role="img" aria-label="Photo of a relaxing spa massage setting with candles" style="left:754px;top:282px;width:290px;height:224px;border-radius:0;background:linear-gradient(180deg,#e9d7c3 0%,#c9a07a 55%,#8a5f3e 100%)"></div>
  <div class="ev-head" style="left:754px;top:520px">SPA <small>(SATURDAY)</small></div>
  <div class="tk" style="left:754px;top:558px"><svg><use href="#tick"/></svg>Limited appointments available</div>
  <div class="tk" style="left:754px;top:586px"><svg><use href="#tick"/></svg>9:30 AM- 3:30 PM ET.</div>
  <div class="pill" style="left:754px;top:616px;width:176px;height:26px;font-size:14px">$150.00 per person</div>
  <div class="tk" style="left:754px;top:656px"><svg><use href="#tick"/></svg>AM or PM Appointment?</div>
  <div class="red" style="left:754px;top:690px">Must have the Phone # of the<br>person with the appointment.</div>
  <div class="blank" style="left:754px;top:726px">Cell # <i style="width:150px;margin-left:10px"></i></div>

  <div class="photo" role="img" aria-label="Photo of shooters at a wooded sporting clay range" style="left:754px;top:794px;width:290px;height:226px;border-radius:0;background:linear-gradient(180deg,#5d6f45 0%,#3e4a2e 55%,#6b5a3a 100%)"></div>
  <div class="ev-head" style="left:754px;top:1034px">SPORTING CLAY <small>(SATURDAY)</small></div>
  <div class="ev-text" style="left:754px;top:1070px;white-space:nowrap">Cedar Run Hunting Club &amp; Sporting Clay</div>
  <div class="tk" style="left:754px;top:1096px"><svg><use href="#tick"/></svg>725 Hollow Road,<br>Owenton, KY 40359 US</div>
  <div class="bul" style="left:776px;top:1142px">55 Minutes from the hotel</div>
  <div class="t" style="left:754px;top:1164px;font-size:15px;color:var(--blue);font-weight:600">www.cedarrunclub.com</div>
  <div class="pill" style="left:754px;top:1192px;width:176px;height:26px;font-size:14px">$150.00 per person</div>
  <div class="ev-text" style="left:754px;top:1228px;white-space:nowrap">Fees include food, drinks, snacks &amp; ammo.</div>
  <div class="red" style="left:754px;top:1256px">Must have the email address of the<br>person shooting.</div>
  <div class="blank" style="left:754px;top:1292px">Email <i style="width:170px;margin-left:10px"></i></div>
  <div class="blank" style="left:754px;top:1324px">What Gauge, 20 or 12? <i style="width:86px;margin-left:8px"></i></div>

  <div class="q-tab">QUESTIONS</div>
  <footer class="footer">
    <div class="footer-left"></div>
    <div class="contact">CONTACT DANA WHITLOCK<br>270-555-0163<br>dwhitlock@triverwing.org</div>
    <div class="deadline"><span class="gold">DEADLINE FOR REGISTRATION: September 15, 2022</span><br>Make checks payable to the Tri-River Wing Federation or pay via<br>credit card using the Registration form.EmailRegistration Forms to<br><i>Email Registration Forms to: <b>dwhitlock@triverwing.org</b></i></div>
    <div class="mail">Mail payment and<br>this registration form to<br><b>410 Maple Station,<br>Bardwell, KY 42023</b></div>
  </footer>
</section>
</body>
</html>
```